Website Performance Testing eBook for the software testing industry

Overview:
I would like an ebook/whitepaper designed. This ebook will be digital published on my website as a lead generation piece. The purpose is to give high level tips on what to look for and things to think about when working on a website performance testing project.
The ebook also demonstrates our expertise and knowledge on the topic.
Topic:
This is an ebook on software testing. Specifically, website performance testing.
About Tervalo:
Tervalo Solutions is an outsourcing development and software testing firm, and we provide expert services for application development, testing and data analytics. We extend our clients’ software testing capabilities with on-demand technical expertise. Our quality assurance resources work as part of our clients’ teams to help test applications on time and within budget.
Our model is designed to allocate the right mix of local and offshore resources in order to optimize expertise, speed and cost. We provide the ability to quickly add specialty skills to our client’s development team without them incurring long-term costs. The result is far better management of resource capacities and outcomes.
Background on our branding and previous pieces:
I have included a few of our previous ebooks and whitepapers. I like the look and feel of these pieces, however we have made updates to our brand guidelines since them, so the new brand guidelines will need to be incorporated, and I'd like to refresh/update what we have done in the past.
Refer to our website for an idea of our look and feel. This page is one of our newer sections and would be a good reference:
http://www.tervalo.example/data-analytics/
Tone and feel:
- The look and feel should be professional, clean and polished.
- I like good use of whitespace.
- I would prefer to keep stock photography of people to a minimum. Any images should add to the content and be relevant to the content.
(Also, I uploaded some InDesign files in case you wanted to refer to those assets, but I didn't include the Links folder because they were too big. If there's anything you more you need, let me know)
Target Market(s)
Audience:
The audience is senior Quality Assurance and Software Testing professionals.
- 30-45 years old
- Technical mindset
- Interested in learning
Titles include
- QA Lead
- QA Manager
- QA Director
- Director or VP of Development
- QA Automation Engineer
Our customers are medium to large sized companies. Many are software companies, but many are also enterprises in all almost all industries.

```html
<!DOCTYPE html>
<html lang="en">
<head>
<meta charset="utf-8">
<title>Website Performance Testing – Cloud Benefits</title>
<link href="https://fonts.googleapis.com/css2?family=Open+Sans:wght@300;400;600&display=swap" rel="stylesheet">
<style>
  :root {
    --brand-red: #e8392a;
    --heading-grey: #b9bec6;
    --body-grey: #555a60;
    --header-grey: #5c6166;
    --rule-grey: #d3d5d8;
    --paper: #ffffff;
  }
  * { margin: 0; padding: 0; box-sizing: border-box; }
  html, body {
    width: 927px; height: 1200px; overflow: hidden;
    background: var(--paper);
    font-family: "Open Sans", sans-serif;
  }
  .page { position: relative; width: 927px; height: 1200px; }

  .running-head {
    position: absolute; left: 54px; top: 73px;
    font-size: 13.2px; font-weight: 400; color: var(--header-grey);
  }
  .brand {
    position: absolute; right: 66px; top: 62px;
    font-size: 30px; font-weight: 400; color: var(--brand-red);
    letter-spacing: -0.3px; line-height: 1;
  }
  .head-rule {
    position: absolute; left: 54px; top: 108px; width: 819px;
    height: 1px; background: var(--rule-grey);
  }

  .chapter-bar {
    position: absolute; left: 97px; top: 166px;
    width: 2px; height: 106px; background: var(--brand-red);
  }
  .chapter-title {
    position: absolute; left: 126px; top: 181px;
    font-size: 36px; font-weight: 300; line-height: 38px;
    color: var(--brand-red); text-transform: uppercase; letter-spacing: 0.2px;
    white-space: nowrap;
  }

  .section-title {
    position: absolute; left: 110px;
    font-size: 23.8px; font-weight: 600; color: var(--heading-grey);
    text-transform: uppercase; letter-spacing: 0.2px; white-space: nowrap;
  }
  .body-copy {
    position: absolute; left: 110px; width: 720px;
    font-size: 15px; font-weight: 300; color: var(--body-grey);
  }
  .body-copy.loose { line-height: 27.3px; }
  .body-copy.tight { line-height: 21.6px; }

  .page-number {
    position: absolute; left: 817px; top: 1123px;
    font-size: 15px; font-weight: 300; color: var(--brand-red);
  }
</style>
</head>
<body>
<div class="page">
  <header>
    <div class="running-head">Website Performance Testing</div>
    <div class="brand">tervalo</div>
    <div class="head-rule"></div>
  </header>

  <div class="chapter-bar"></div>
  <h1 class="chapter-title">Cloud Benefits for Website<br>Performance Testing</h1>

  <h2 class="section-title" style="top:325px">Realistic Performance Evaluation</h2>
  <p class="body-copy loose" style="top:400px">Cloud-based performance testing supplies more realistic conditions beyond the corporate intra-net including those out of your control. Such conditions include unpredictable peak or event loading, network congestion or a varying device and browser mix. It also offers opportunities to performance test across global regions and time zones.</p>
  <p class="body-copy loose" style="top:551px">For example, your testing can take advantage of virtual infrastructure over specific or multiple regions, which might uncover issues with local network infrastructure, regional user conventions, translations or issues with large content delivery. The latter might, for instance, be alleviated by the use of a cloud-based CDN on a per-region basis.</p>

  <h2 class="section-title" style="top:707px">Instant Swap of Test and Deployment</h2>
  <p class="body-copy tight" style="top:786px">Cloud-based testing has process advantages as well. The use of virtual server infrastructure plus state-of-the-art deployment tools offered by the best cloud providers enables testing different software versions by swapping instances within seconds.</p>
  <p class="body-copy tight" style="top:893px">For instance, instrumented test versions of your website could be exchanged almost immediately with the deployed version by redirecting your site address to the test version via saved infrastructure configurations. These are stored in version control along with the site and test code.</p>

  <div class="page-number">7</div>
</div>
</body>
</html>
```